Lumacraftery 'Quiet Harbour' Book Cover Design project

I need to revise the book cover design I have for my coming book. The design I created through PixelGuild is great but the book has grown and changed so I'm looking for an alternative/option design. I can then choose later from the different options.

I need a book cover that represents the unique book I am creating.

Book Title:
The Open Meadow

Subtitle: Walking Forward Beyond Every Box

The book is targeting all readers with a special focus on same sex attracted readers. It should not have stereotypical images.

I am including a file of the book cover I have had designed. The back cover blurb, author info and author pic will remain the same. The colouring of the back cover and spine will, of course, change to match the colouring of the front cover.

The new title will be on the spine and the new title wording.

The front cover will be markedly different using the bold images and rainbow colours of the images found in the files I am uploading for you.

I am thinking of a large boldly coloured rainbow face with the title and subtitle ON the image. The image will be the whole cover. It will fill the cover as much as possible with the text added onto the pic.

The bold pictures I am including will give you the idea of what I'm looking for.

ANY of the images I've uploaded can be used as the actual front cover image OR the designer might have/find some suitable image to be used. The image is to be large and bold and fill the cover. Hopefully a positive energy.
It needs to be eye-catching and striking and bold and positive.

So...the book cover sample file I've provided can keep the back cover with completely new colouring. The front cover is completely new with new image, wording and energy.

It is to be a rainbow coloured face or figure for the cover image.

I hope that is clear enough for you. I'm very happy to discuss and clarify these ideas with the designer. Looking forward to another great PixelGuild experience.

Target Market(s)

Wide audience with special focus on Same Sex Attracted individuals

Font styles to use
Script
Other font styles liked:
• Some form of handwriting font to make the book title and text appear more personal....as if handwritten by me.

Requirements
Must have
• Boldness, Quirky, Rainbow Colour, Image to fill the cover, maybe dark cover contrasting background.
Nice to have
• A well balanced back cover especially in the area where the barcode will be placed.
Should not have
• No stereotypical images

```html
<!DOCTYPE html>
<html lang="en">
<head>
<meta charset="utf-8">
<title>The Open Meadow – Book Cover Wrap</title>
<link rel="stylesheet" href="https://fonts.googleapis.com/css2?family=Amatic+SC:wght@700&family=Oswald:wght@300;500;700&family=Libre+Baskerville:ital,wght@0,400;0,700;1,400&family=Caveat+Brush&family=Dancing+Script:wght@600&display=swap">
<style>
  :root{
    --ink:#000;
    --paper:#fff;
    --magenta:#c8245f;
    --magenta-deep:#8e1747;
    --tag-text:#b9bcbf;
    --brand-gold:#f2a93b;
  }
  *{margin:0;padding:0;box-sizing:border-box}
  html,body{width:1200px;height:927px;overflow:hidden;background:var(--ink)}
  .wrap{position:relative;width:1200px;height:927px;background:var(--ink);color:var(--paper)}

  /* Back cover */
  .back{position:absolute;left:0;top:0;width:572px;height:927px}
  .back-quote{position:absolute;left:20px;top:26px;width:530px;text-align:center;
    font-family:"Amatic SC",cursive;font-weight:700;font-size:24px;line-height:28px;
    letter-spacing:1px;text-transform:uppercase;white-space:nowrap}
  .headline{position:absolute;left:20px;top:146px;width:532px;text-align:center;white-space:nowrap;
    font-family:"Oswald",sans-serif;font-weight:700;font-size:20px;letter-spacing:.4px;line-height:26px}
  .subhead{position:absolute;left:20px;top:181px;width:532px;text-align:center;white-space:nowrap;
    font-family:"Oswald",sans-serif;font-weight:700;font-size:15px;letter-spacing:-.5px;line-height:20px}
  .blurb{position:absolute;left:54px;width:474px;font-family:"Libre Baskerville",serif;
    font-size:13.6px;line-height:19.5px;text-align:justify}
  .blurb-one{top:216px}
  .blurb-two{top:322px}
  .blurb-three{top:562px}
  .pull-band{position:absolute;left:0;top:444px;width:572px;height:102px}
  .pull-quote{position:absolute;left:52px;top:461px;width:482px;
    font-family:"Oswald",sans-serif;font-weight:500;font-style:italic;font-size:14px;line-height:20px;
    letter-spacing:.9px;transform:skewX(-8deg)}
  .author-photo{position:absolute;left:37px;top:636px;width:195px;height:142px;
    background:linear-gradient(135deg,#3f4a2c,#6c7b45 45%,#2c3320)}
  .author-info{position:absolute;left:242px;top:636px;width:320px}
  .author-name{font-family:"Libre Baskerville",serif;font-weight:700;font-size:15.5px;margin-bottom:2px}
  .author-bio{font-family:"Libre Baskerville",serif;font-style:italic;font-size:13.2px;line-height:18.5px}
  .author-bio b{font-style:italic}
  .author-url{font-family:"Libre Baskerville",serif;font-weight:700;font-size:16.5px;margin-top:6px}
  .brand{position:absolute;left:37px;top:788px;width:195px;height:114px;background:#0b0b0b;
    display:flex;flex-direction:column;align-items:center;justify-content:flex-end;padding-bottom:14px}
  .brand-name{font-family:"Oswald",sans-serif;font-weight:500;font-size:18px;letter-spacing:.3px;color:var(--brand-gold)}
  .brand-tag{font-family:"Oswald",sans-serif;font-weight:300;font-size:6.5px;letter-spacing:.3px;margin-top:2px}
  .barcode-area{position:absolute;left:376px;top:800px;width:168px;height:102px;background:var(--paper)}

  /* Spine */
  .spine{position:absolute;left:572px;top:0;width:56px;height:927px}
  .spine-title{position:absolute;left:8px;top:96px;writing-mode:vertical-rl;white-space:nowrap;
    font-family:"Caveat Brush",cursive;font-size:32px;letter-spacing:1px;text-transform:uppercase}
  .spine-author{position:absolute;left:14px;top:468px;writing-mode:vertical-rl;text-orientation:upright;
    white-space:nowrap;font-family:"Oswald",sans-serif;font-weight:300;font-size:18px;letter-spacing:8px}

  /* Front cover */
  .front{position:absolute;left:628px;top:0;width:572px;height:927px;overflow:hidden}
  .cover-art{position:absolute;inset:0;
    background:
      radial-gradient(ellipse 45% 30% at 40% 30%,rgba(230,40,150,.85),transparent 70%),
      radial-gradient(ellipse 35% 25% at 70% 15%,rgba(240,180,40,.8),transparent 70%),
      radial-gradient(ellipse 40% 30% at 30% 60%,rgba(40,170,200,.7),transparent 70%),
      radial-gradient(ellipse 40% 30% at 20% 85%,rgba(230,220,40,.75),transparent 70%),
      radial-gradient(ellipse 35% 30% at 85% 55%,rgba(120,30,20,.8),transparent 70%),
      linear-gradient(160deg,#2a1a12,#5a2a24 40%,#1b2a22 75%,#10120e)}
  .title{position:absolute;left:128px;top:470px;font-family:"Caveat Brush",cursive;font-weight:400;
    text-transform:uppercase;line-height:.86;transform:rotate(-5deg);transform-origin:left top;
    white-space:nowrap;text-shadow:0 2px 6px rgba(0,0,0,.5)}
  .title span{display:block}
  .title-one{font-size:88px;margin-left:14px}
  .title-two{font-size:112px}
  .tag-wrap{position:absolute;left:140px;top:690px;width:330px;height:142px;transform:rotate(-10deg)}
  .tag-shape{position:absolute;inset:0;background:linear-gradient(135deg,#4a4b4e,#2d2e30);
    clip-path:polygon(14% 0,100% 0,100% 100%,14% 100%,0 50%)}
  .tag-hole{position:absolute;left:26px;top:63px;width:16px;height:16px;border-radius:50%;
    background:#7a6f5c;border:3px solid #b8ab8f}
  .subtitle{position:absolute;left:60px;top:36px;width:260px;font-family:"Dancing Script",cursive;
    font-weight:600;font-size:25px;line-height:34px;color:var(--tag-text);text-align:center;white-space:nowrap}
  .front-author{position:absolute;left:104px;top:858px;white-space:nowrap;font-family:"Oswald",sans-serif;
    font-weight:300;font-size:44px;letter-spacing:15px;line-height:1}
</style>
</head>
<body>
<main class="wrap">
  <section class="back">
    <p class="back-quote">"It's important to challenge our accepted beliefs and<br>the stories we tell ourselves, individually and as a<br>community, if there is to be any sense of wholeness,<br>happiness and future."</p>
    <h2 class="headline">YOUR RAINBOW IS MUCH MORE THAN THE FLAG YOU WAVE.</h2>
    <p class="subhead">IT IS THE UNIQUE AND INDIVIDUAL YOU BEHIND THE LAYERS, LABELS AND STORIES.</p>
    <p class="blurb blurb-one">This first book by Alden Marsh asks each of us to consider our accepted beliefs and personal stories as we explore the possible ways to LIVE OUR LIFE AND NOT A LABEL. Doing this requires some honest inner work and a journey that will need to be passionately personal and authentically individual.</p>
    <p class="blurb blurb-two">‘The Open Meadow’ reminds us that a beautiful, rainbow life is more than sexuality, personality or gender or having a camp, team or tribe to belong to. It is much more than any acronym, scene or lifestyle. It’s ‘an inside job’, deeply heartfelt and courageously unique. Finding and living the YOU of YOU has boldness and power and magic in it.</p>
    <svg class="pull-band" viewBox="0 0 572 102" preserveAspectRatio="none" aria-hidden="true">
      <path d="M300 0 H560 V6 H300 Z" fill="var(--magenta)"/>
      <path d="M0 14 H548 L552 88 H0 Z" fill="var(--magenta-deep)"/>
      <path d="M0 18 H545 V84 H0 Z" fill="var(--magenta)"/>
      <path d="M0 94 H250 V100 H0 Z" fill="var(--magenta)"/>
    </svg>
    <p class="pull-quote">"LIVING A MEANINGFUL, HAPPY EXISTENCE IS ABOUT BEING TRUE TO THE WHOLE, COMPLEX, INTEGRATED PERSON THAT YOU ARE AND BEING STRONG ENOUGH AND AWARE ENOUGH AND REFLECTIVE ENOUGH TO KNOW YOURSELF, LOVE YOURSELF AND BE YOURSELF" ALDEN MARSH</p>
    <p class="blurb blurb-three">This simple and insightful book will help you explore ways to bravely and honestly know, love and be yourself no matter what the rest of the world might be doing or saying or expecting.</p>
    <div class="author-photo" role="img" aria-label="Author portrait photograph, seated outdoors among greenery"></div>
    <div class="author-info">
      <p class="author-name">ALDEN MARSH</p>
      <p class="author-bio">Personal Change and Relationships Coach.<br><b>LUMACRAFTERY</b> Coaching and Wellness.<br>Advocate, Activist, Writer and support<br>for MEN WHO DATE MEN and their<br>Wholeness, Happiness and Human Rights.</p>
      <p class="author-url">www.lumacraftery-coach.net</p>
    </div>
    <div class="brand">
      <span class="brand-name">LUMACRAFTERY</span>
      <span class="brand-tag">COACHING•SUPPORT•WORKSHOPS•RETREATS</span>
    </div>
    <div class="barcode-area" aria-hidden="true"></div>
  </section>

  <section class="spine">
    <p class="spine-title">The Open Meadow</p>
    <p class="spine-author">ALDEN MARSH</p>
  </section>

  <section class="front">
    <div class="cover-art" role="img" aria-label="Close-up portrait photograph covered in bold rainbow paint in pink, yellow, teal and orange"></div>
    <h1 class="title"><span class="title-one">The Open</span><span class="title-two">Meadow</span></h1>
    <div class="tag-wrap">
      <div class="tag-shape"></div>
      <div class="tag-hole"></div>
      <p class="subtitle">Walking Forward<br>Beyond Every Box</p>
    </div>
    <p class="front-author">ALDEN MARSH</p>
  </section>
</main>
</body>
</html>
```